Flyer-Design für eine Band
Zielgruppe
Bandname 'Klangwerk'
Musiker
Coverband für Hochzeiten, Events und Partymusik
Zielgruppe sind Leute (jung und alt) die stimmungsvolle Musik für Ihre Veranstaltung suchen
Aufgabenstellung
Die Werbekarte soll zu unserem bisherigen Stil laut Social Media bzw. Homepage passen.
Wir möchen gerne unser(e) Foto(s) aus unserem Fotoshooting verwenden.
Wir hätten gerne eine Werbekarte im Postkartenformat (vorne und hinten bedruckt)
Angeführt soll sein:
- die Webseite (https://klangwerk-beispiel.at)
- email (kontakt@klangwerk-beispiel.at)
- Telefonnummer (0664 218 57 903)

```html
<!DOCTYPE html>
<html lang="de">
<head>
<meta charset="utf-8">
<title>Klangwerk – Werbekarte</title>
<link rel="stylesheet" href="https://fonts.googleapis.com/css2?family=Bitter:wght@400;500;700&display=swap">
<style>
  :root {
    --paper: #ffffff;
    --ink: #1c1c1c;
    --band: #7fcfe0;
    --brand: #8fd4e2;
    --photo-light: #c9c6c0;
    --photo-dark: #8a857c;
  }
  * { margin: 0; padding: 0; box-sizing: border-box; }
  html, body { width: 1200px; height: 849px; overflow: hidden; background: var(--paper); }
  body { font-family: "Bitter", Georgia, serif; color: var(--ink); }
  .card { position: relative; width: 1200px; height: 849px; background: var(--paper); overflow: hidden; }

  .band-photo {
    position: absolute; left: 0; top: 0; width: 442px; height: 655px;
    background: linear-gradient(90deg, var(--photo-dark) 0%, var(--photo-light) 35%, var(--photo-dark) 60%, var(--photo-light) 100%);
  }

  .brand {
    position: absolute; left: 905px; top: 30px; display: flex; align-items: center; gap: 14px;
  }
  .brand-dot { width: 40px; height: 40px; border: 3px solid var(--brand); border-radius: 50%; }
  .brand-name { font-size: 42px; font-weight: 400; color: var(--brand); line-height: 1; }

  .offer-title {
    position: absolute; left: 570px; top: 150px;
    font-size: 36px; font-weight: 700;
  }
  .offer-list {
    position: absolute; left: 498px; top: 252px; list-style: none;
    font-size: 28px; font-weight: 500; line-height: 37px;
  }
  .offer-list .wrap { padding-left: 30px; display: block; }

  .contact-band {
    position: absolute; left: 0; top: 655px; width: 1200px; height: 194px; background: var(--band);
  }
  .contact-title {
    position: absolute; left: 128px; top: 36px; font-size: 33px; font-weight: 700;
  }
  .contact-item {
    position: absolute; top: 106px; display: flex; align-items: center; gap: 14px;
    font-size: 23px; font-weight: 500;
  }
  .contact-item svg { width: 30px; height: 30px; fill: none; stroke: var(--ink); stroke-width: 1.6; }
  .contact-web { left: 24px; }
  .contact-mail { left: 424px; }
  .contact-phone { left: 842px; }
</style>
</head>
<body>
<div class="card">
  <div class="band-photo" role="img" aria-label="Foto der beiden Musiker mit Gitarre vor einer Holzwand"></div>

  <div class="brand">
    <span class="brand-dot"></span>
    <span class="brand-name">klangwerk</span>
  </div>

  <h1 class="offer-title">Was bieten wir Euch?</h1>
  <ul class="offer-list">
    <li>- Perfekte Abstimmung eurer Wünsche mit<span class="wrap">unserem Portfolio</span></li>
    <li>- Eigenes Equipment</li>
    <li>- Zuverlässigkeit</li>
    <li>- Professionelle Vorbereitung und Darbietung</li>
    <li>- Unkomplizierte Abwicklung</li>
    <li>- Fixpreis – keine versteckten Kosten</li>
  </ul>

  <footer class="contact-band">
    <h2 class="contact-title">Kontakt</h2>
    <div class="contact-item contact-web">
      <svg viewBox="0 0 24 24"><circle cx="12" cy="12" r="10"/><ellipse cx="12" cy="12" rx="4.5" ry="10"/><line x1="2" y1="12" x2="22" y2="12"/><path d="M4 7h16M4 17h16"/></svg>
      <span>klangwerk-beispiel.at</span>
    </div>
    <div class="contact-item contact-mail">
      <svg viewBox="0 0 24 24"><rect x="2" y="5" width="20" height="14"/><path d="M2 5l10 8 10-8"/></svg>
      <span>kontakt@klangwerk-beispiel.at</span>
    </div>
    <div class="contact-item contact-phone">
      <svg viewBox="0 0 24 24"><path d="M5 3h4l2 5-2.5 1.5a11 11 0 0 0 6 6L16 13l5 2v4a2 2 0 0 1-2 2A17 17 0 0 1 3 5a2 2 0 0 1 2-2z"/></svg>
      <span>0664 218 57 903</span>
    </div>
  </footer>
</div>
</body>
</html>
```